Lucien Marchand

Changes to attached business card: 1. Eliminate borders (black) top and bottom of the existing card. 2- eliminate: Become the reference! 3- adding: www.doublezvoschiffres.ca info@doublezvoschiffres.ca lucienmarchandconseil.com (819) 555-2736 4- black on white

Contact Information for Business Card

voir pièce ci-jointe pour exemple

Requirements
Must have
• black on white
Nice to have
• Very modern ! with punch!

```html
<!DOCTYPE html>
<html lang="fr">
<head>
<meta charset="utf-8">
<title>Lucien Marchand – Carte d'affaires</title>
<link href="https://fonts.googleapis.com/css2?family=Cinzel:wght@400;700&family=Lato:wght@400;700;900&family=Cormorant+Garamond:wght@500&display=swap" rel="stylesheet">
<style>
  :root {
    --page-bg: #e9e6e1;
    --card-white: #ffffff;
    --card-edge: #f3f3f3;
    --panel-light: #f1f1f1;
    --panel-border: #dcdcdc;
    --text-black: #111111;
    --text-soft: #2b2b2b;
    --rule: #1a1a1a;
    --photo-light: #e6e1dc;
    --photo-dark: #6d5a50;
  }
  * { margin: 0; padding: 0; box-sizing: border-box; }
  html, body { width: 1200px; height: 1023px; overflow: hidden; }
  body {
    background: var(--page-bg);
    position: relative;
    font-family: "Lato", sans-serif;
  }
  .business-card {
    position: absolute;
    left: 75px;
    top: 211px;
    width: 1050px;
    height: 600px;
    border-radius: 6px;
    background: linear-gradient(160deg, var(--card-white) 0%, var(--card-white) 55%, var(--card-edge) 100%);
    box-shadow: 0 18px 40px rgba(0,0,0,0.25);
    color: var(--text-black);
    overflow: hidden;
  }
  .identity {
    position: absolute;
    left: 70px;
    top: 300px;
  }
  .identity-name {
    font-family: "Cinzel", serif;
    font-weight: 700;
    font-size: 46px;
    letter-spacing: 1px;
    line-height: 1;
  }
  .identity-role {
    display: flex;
    align-items: center;
    gap: 10px;
    margin-top: 8px;
    font-family: "Cormorant Garamond", serif;
    font-size: 21px;
    color: var(--text-soft);
  }
  .identity-role::before {
    content: "";
    width: 70px;
    height: 2px;
    background: var(--rule);
  }
  .identity-rule {
    margin-top: 16px;
    width: 400px;
    height: 2px;
    background: var(--rule);
  }
  .contact-list {
    position: absolute;
    left: 70px;
    top: 470px;
    list-style: none;
    font-size: 22px;
    color: var(--text-soft);
  }
  .contact-list li {
    display: flex;
    align-items: center;
    gap: 16px;
    height: 34px;
  }
  .contact-list svg { width: 20px; height: 20px; fill: var(--text-black); flex: none; }
  .portrait-panel {
    position: absolute;
    right: 60px;
    top: 40px;
    width: 420px;
    height: 360px;
    border-radius: 18px;
    background: var(--panel-light);
    border: 1px solid var(--panel-border);
  }
  .portrait-photo {
    position: absolute;
    left: 18px;
    top: 18px;
    width: 382px;
    height: 270px;
    border: 6px solid var(--text-black);
    background: radial-gradient(circle at 40% 45%, var(--photo-dark) 0%, #8c786c 35%, var(--photo-light) 70%, #f7f5f2 100%);
  }
  .portrait-name {
    position: absolute;
    left: 0;
    right: 0;
    bottom: 22px;
    text-align: center;
    font-size: 32px;
    letter-spacing: 0.5px;
    color: var(--text-black);
  }
  .portrait-name strong { font-weight: 900; }
  .web-invite {
    position: absolute;
    right: 60px;
    top: 430px;
    width: 460px;
    font-size: 21px;
    line-height: 1.5;
    color: var(--text-soft);
  }
</style>
</head>
<body>
  <section class="business-card">
    <div class="identity">
      <div class="identity-name">Lucien Marchand</div>
      <div class="identity-role">Consultant - Coach</div>
      <div class="identity-rule"></div>
    </div>

    <ul class="contact-list">
      <li>
        <svg viewBox="0 0 24 24" aria-hidden="true"><path d="M6.6 10.8a15.1 15.1 0 0 0 6.6 6.6l2.2-2.2c.3-.3.7-.4 1-.2 1.1.4 2.3.6 3.6.6.6 0 1 .4 1 1V20c0 .6-.4 1-1 1C10.6 21 3 13.4 3 4c0-.6.4-1 1-1h3.5c.6 0 1 .4 1 1 0 1.3.2 2.5.6 3.6.1.3 0 .7-.2 1z"/></svg>
        (819) 555-2736
      </li>
      <li>
        <svg viewBox="0 0 24 24" aria-hidden="true"><path d="M2 5h20v14H2z M4 7v.4l8 5.2 8-5.2V7z"/></svg>
        info@doublezvoschiffres.ca
      </li>
      <li>
        <svg viewBox="0 0 24 24" aria-hidden="true"><path d="M12 2a10 10 0 1 0 0 20 10 10 0 0 0 0-20zm6.9 9h-3a15 15 0 0 0-1.3-5.6A8 8 0 0 1 18.9 11zM12 4.1c.9 1.2 1.8 3.6 1.9 6.9h-3.8c.1-3.3 1-5.7 1.9-6.9zM9.4 5.4A15 15 0 0 0 8.1 11h-3a8 8 0 0 1 4.3-5.6zM5.1 13h3a15 15 0 0 0 1.3 5.6A8 8 0 0 1 5.1 13zm6.9 6.9c-.9-1.2-1.8-3.6-1.9-6.9h3.8c-.1 3.3-1 5.7-1.9 6.9zm2.6-1.3a15 15 0 0 0 1.3-5.6h3a8 8 0 0 1-4.3 5.6z"/></svg>
        lucienmarchandconseil.com
      </li>
    </ul>

    <div class="portrait-panel">
      <div class="portrait-photo" role="img" aria-label="Photo portrait de Lucien Marchand"></div>
      <div class="portrait-name"><strong>LUCIEN</strong> MARCHAND</div>
    </div>

    <p class="web-invite">
      Visitez mon site web! Consultation gratuite et sans obligation.<br>
      www.doublezvoschiffres.ca
    </p>
  </section>
</body>
</html>
```